Med Spa business card design with logo

Need a logo design and business card for our new company Verbena Aesthetics Med Spa. We are a medical office that deals with high end clients. We offer them skin care products which include DERMIQ, lip augmentation, and various laser for the skin. I king of like the logo attached, maybe something along those lines but also open to any logo concept.
Updates

Target Market(s)

Out target audience are male and females in the age range of 21-80 years of age

Industry/Entity Type

Medical

Contact Information for Business Card

woukd like front of card to have logo and business name VERBENA AESTHETICS MEDSPA. Back of card employee name and phone number along with instagram logo and user name

Font styles to use
Serif
Sans Serif

Requirements
Must have
• prefer monochromatic look white, black, gold
Should not have
• not too colorful

```html
<!DOCTYPE html>
<html lang="en">
<head>
<meta charset="utf-8">
<title>Verbena Aesthetics Med Spa – Business Card</title>
<link href="https://fonts.googleapis.com/css2?family=Oswald:wght@500&family=Open+Sans:wght@400;600&display=swap" rel="stylesheet">
<style>
  :root {
    --backdrop: #2a2a2a;
    --card: #34322c;
    --card-deep: #2d2b27;
    --band-light: #8a8a88;
    --band-dark: #4a4946;
    --ink-white: #f4f4f2;
    --ink-grey: #8e8d89;
    --ink-soft: #d8d8d5;
  }
  html, body {
    margin: 0;
    width: 1200px;
    height: 1000px;
    overflow: hidden;
    background: var(--backdrop);
    font-family: "Open Sans", sans-serif;
  }
  .canvas {
    position: relative;
    width: 1200px;
    height: 1000px;
  }
  .card {
    position: absolute;
    left: 200px;
    width: 800px;
    height: 440px;
    background: linear-gradient(160deg, var(--card), var(--card-deep));
    box-shadow: 0 10px 30px rgba(0,0,0,0.45);
    overflow: hidden;
  }
  .card--front { top: 50px; }
  .card--back { top: 530px; }
  .band {
    position: absolute;
    left: 0;
    right: 0;
    bottom: 30px;
    height: 58px;
    background: linear-gradient(90deg, var(--band-dark), var(--band-light) 55%, var(--band-dark));
    display: flex;
    align-items: center;
    justify-content: center;
    color: var(--ink-white);
    letter-spacing: 1.5px;
    font-weight: 600;
  }
  .band__title { font-size: 20px; }
  .band__address { font-size: 22px; font-weight: 400; letter-spacing: 2px; }
  .band__mark {
    position: absolute;
    right: 22px;
    top: 50%;
    width: 34px;
    height: 34px;
    margin-top: -17px;
    border-radius: 50%;
    border: 2px solid var(--ink-soft);
    box-sizing: border-box;
  }
  .brand {
    position: absolute;
    top: 110px;
    left: 0;
    right: 0;
    display: flex;
    align-items: center;
    justify-content: center;
    gap: 16px;
  }
  .brand__mark {
    width: 56px;
    height: 56px;
    border-radius: 50%;
    border: 3px solid var(--ink-soft);
    box-sizing: border-box;
  }
  .brand__name {
    font-size: 34px;
    font-weight: 600;
    letter-spacing: 6px;
    color: var(--ink-soft);
  }
  .identity {
    position: absolute;
    top: 150px;
    left: 120px;
    display: flex;
    align-items: center;
  }
  .identity__person { text-align: right; padding-right: 22px; }
  .identity__name {
    font-family: "Oswald", sans-serif;
    font-weight: 500;
    font-size: 48px;
    line-height: 1;
    letter-spacing: 2px;
    color: var(--ink-white);
  }
  .identity__role {
    margin-top: 6px;
    font-size: 19px;
    letter-spacing: 1px;
    color: var(--ink-grey);
  }
  .identity__divider {
    width: 2px;
    height: 96px;
    background: var(--ink-soft);
  }
  .contacts {
    list-style: none;
    margin: 0;
    padding: 0 0 0 22px;
  }
  .contacts__item {
    display: flex;
    align-items: center;
    gap: 22px;
    height: 32px;
    font-size: 21px;
    color: var(--ink-soft);
    letter-spacing: 0.5px;
  }
  .contacts__icon { width: 16px; height: 16px; fill: var(--ink-grey); }
</style>
</head>
<body>
<main class="canvas">
  <section class="card card--front" aria-label="Card front">
    <div class="brand">
      <span class="brand__mark"></span>
      <span class="brand__name">VERBENA</span>
    </div>
    <div class="band">
      <span class="band__title">VERBENA AESTHETICS MEDSPA</span>
      <span class="band__mark"></span>
    </div>
  </section>

  <section class="card card--back" aria-label="Card back">
    <div class="identity">
      <div class="identity__person">
        <div class="identity__name">ADRIAN HALE</div>
        <div class="identity__role">CEO &amp; FOUNDER</div>
      </div>
      <div class="identity__divider"></div>
      <ul class="contacts">
        <li class="contacts__item">
          <svg class="contacts__icon" viewBox="0 0 16 16"><path d="M3 1l3 3-1.5 2c1 2 3 4 5 5L11.5 9.5l3 3L12 15C6 14 2 10 1 4z"/></svg>
          +1 212 555 0147
        </li>
        <li class="contacts__item">
          <svg class="contacts__icon" viewBox="0 0 16 16"><path d="M1 3h14v10H1z M1 3l7 6 7-6" fill="var(--ink-grey)" stroke="var(--card)" stroke-width="1"/></svg>
          adrian@verbenamedspa.com
        </li>
        <li class="contacts__item">
          <svg class="contacts__icon" viewBox="0 0 16 16"><circle cx="8" cy="8" r="7"/><path d="M1 8h14M8 1c-3 4-3 10 0 14M8 1c3 4 3 10 0 14" stroke="var(--card)" stroke-width="1" fill="none"/></svg>
          www.verbenamedspa.com
        </li>
      </ul>
    </div>
    <div class="band">
      <span class="band__address">48 ELMWOOD AVENUE, NEW YORK CITY, 10021</span>
    </div>
  </section>
</main>
</body>
</html>
```